Real estate company needs a letterhead design

A young real estate company needs a letterhead / stationery design, it should include the company's logo. It should look exactly the same as on the business cards. (With the phrase "a brand of FEO Immobilien & Projektentwicklung GmbH")

In addition, it should also include the 4 round seals.

color code blue # 00456b gray # 333333

Word and PDF are welcome.

FEO Immobilien & Projektentwicklung GmbH
Managing director: Mag. Lukas Strenhofer
Anton-Wiesmayr-Strasse 3c / 41
6342 Talbrunn

Tel .: +436645917283
Email: office@wohnquell.example
Web: www.wohnquell.example

Sparkasse Almhofen, Bergländer Sparkasse from 1893, Gildenkasse
Ferdinand-Moosrainer-Strasse 9, 6342 Talbrunn
IBAN: AT31 4819 2093 5521 6604
BIC: GLMRAT31XXX
Account holder: FEO Immobilien & Projektentwicklung GmbH

FN: XXXXXXX
UID: XXXXXXX

```html
<!DOCTYPE html>
<html lang="de">
<head>
<meta charset="utf-8">
<title>WOHNQUELL – Briefpapier</title>
<link href="https://fonts.googleapis.com/css2?family=Poppins:wght@400;600;700&display=swap" rel="stylesheet">
<style>
  :root{
    --backdrop:#e6e6e6;
    --paper:#f2f2f2;
    --brand-blue:#00456b;
    --brand-blue-fold:#002f4a;
    --strip-gray:#444444;
    --strip-mark:#383838;
    --text-light:#ffffff;
    --rule:#8a8a8a;
    --seal-red:#e0302a;
    --seal-ring:#ffffff;
  }
  *{margin:0;padding:0;box-sizing:border-box}
  html,body{width:1200px;height:795px;overflow:hidden}
  body{background:var(--backdrop);font-family:"Poppins",sans-serif;position:relative}

  .letterhead{
    position:absolute;left:333px;top:20px;width:534px;height:755px;
    background:var(--paper);box-shadow:0 4px 18px rgba(0,0,0,.12);
  }
  .side-strip{
    position:absolute;left:0;top:0;width:170px;height:100%;
    background:var(--strip-gray);color:var(--text-light);
  }
  .brand-ribbon{
    position:absolute;left:0;top:26px;width:196px;height:58px;
    background:var(--brand-blue);display:flex;align-items:center;padding-left:20px;z-index:2;
  }
  .brand-ribbon-fold{position:absolute;left:170px;top:14px;z-index:1}
  .brand-name{font-weight:600;font-size:25px;letter-spacing:.5px;color:var(--text-light);line-height:1}

  .contact-block{position:absolute;left:18px;top:110px;right:10px;font-size:7.5px;line-height:1.45}
  .company-name{font-weight:700;text-transform:uppercase;margin-bottom:12px}
  .person-name{font-weight:600}
  .address{margin-bottom:10px}
  .channel{display:flex;align-items:center;gap:5px}
  .channel svg{flex:none}
  .divider{border:0;border-top:1px solid var(--rule);margin:12px 0;width:92%}
  .label{font-weight:700}
  .label-spaced{margin-top:8px}
  .legal{margin-top:18px;font-weight:600}

  .house-mark{position:absolute;left:0;bottom:0;width:170px;height:190px;
    background:linear-gradient(160deg,var(--strip-gray) 0%,var(--strip-mark) 70%)}

  .seal-row{position:absolute;right:40px;bottom:70px;display:flex;gap:22px}
  .seal{width:52px;height:52px;border-radius:50%;background:var(--seal-ring);
    border:1.5px solid var(--seal-red);display:flex;align-items:center;justify-content:center}
  .seal span{width:30px;height:30px;border-radius:50%;background:var(--seal-red);display:block}
</style>
</head>
<body>
  <main class="letterhead">
    <aside class="side-strip">
      <svg class="brand-ribbon-fold" width="30" height="70" viewBox="0 0 30 70" aria-hidden="true">
        <polygon points="0,12 26,0 26,58 0,70" fill="var(--brand-blue-fold)"/>
      </svg>
      <div class="brand-ribbon"><span class="brand-name">WOHNQUELL</span></div>

      <section class="contact-block">
        <p class="company-name">FEO Immobilien &amp;<br>Projektentwicklung GmbH</p>
        <p class="person-name">Mag. Lukas Strenhofer</p>
        <p>Managing director</p>
        <p class="address">Anton-Wiesmayr-Strasse 3c / 41<br>6342 Talbrunn</p>
        <p class="channel">
          <svg width="8" height="8" viewBox="0 0 8 8"><rect width="8" height="8" rx="1.5" fill="#fff"/><path d="M2.2 1.8l1 1-.5.7c.4.8.9 1.3 1.7 1.7l.7-.5 1 1-.7.8C3.8 6.3 1.7 4.2 1.4 2.5z" fill="var(--strip-gray)"/></svg>
          +436645917283</p>
        <p class="channel">
          <svg width="8" height="8" viewBox="0 0 8 8"><rect width="8" height="8" rx="1.5" fill="#fff"/><rect x="1.5" y="2.3" width="5" height="3.4" fill="none" stroke="var(--strip-gray)" stroke-width=".7"/><path d="M1.5 2.3L4 4.3 6.5 2.3" fill="none" stroke="var(--strip-gray)" stroke-width=".7"/></svg>
          office@wohnquell.example</p>
        <p class="channel">
          <svg width="8" height="8" viewBox="0 0 8 8"><rect width="8" height="8" rx="1.5" fill="#fff"/><circle cx="4" cy="4" r="2.5" fill="none" stroke="var(--strip-gray)" stroke-width=".6"/><path d="M1.5 4h5M4 1.5c-1.3 1.5-1.3 3.5 0 5M4 1.5c1.3 1.5 1.3 3.5 0 5" fill="none" stroke="var(--strip-gray)" stroke-width=".5"/></svg>
          www.wohnquell.example</p>

        <hr class="divider">
        <p>Sparkasse Almhofen,<br>Bergländer Sparkasse from 1893,<br>Gildenkasse<br>Ferdinand-Moosrainer-Strasse 9,<br>6342 Talbrunn</p>

        <hr class="divider">
        <p class="label">IBAN:</p>
        <p>AT31 4819 2093 5521 6604</p>
        <p class="label label-spaced">BIC:</p>
        <p>GLMRAT31XXX</p>

        <hr class="divider">
        <p class="label">Account holder:</p>
        <p>FEO Immobilien &amp;<br>Projektentwicklung GmbH</p>

        <p class="legal">FN: XXXXXXX<br>UID: XXXXXXX</p>
      </section>

      <div class="house-mark" role="img" aria-label="Large faint brand house mark as background decoration"></div>
    </aside>

    <div class="seal-row">
      <div class="seal" role="img" aria-label="Certification seal"><span></span></div>
      <div class="seal" role="img" aria-label="Certification seal"><span></span></div>
      <div class="seal" role="img" aria-label="Certification seal"><span></span></div>
      <div class="seal" role="img" aria-label="Certification seal"><span></span></div>
    </div>
  </main>
</body>
</html>
```